Small rum distillery looking for bottle design

Small rum distillery in Estonia. Looking for bottle lable design. It should be simple but at the same time point out from the variety of other bottles.
As we are a small nordic country, design can be some how nordic or represent our country. It can also have some connection with sailing or sea as we know it pirates love it.
Bottle we are using is Calidra 500

food and beverage

• Baskerville

```html
<!DOCTYPE html>
<html lang="en">
<head>
<meta charset="utf-8">
<title>Harka Distillery – Rum Label</title>
<link href="https://fonts.googleapis.com/css2?family=Libre+Baskerville:wght@400;700&display=swap" rel="stylesheet">
<style>
  :root {
    --page: #ffffff;
    --sky-top: #1f8cdb;
    --sky-mid: #62b0e6;
    --dawn: #f5c6a3;
    --sea: #45b1e0;
    --frame-red: #d9262b;
    --frame-white: #ffffff;
    --oval: #3b3b3d;
    --ink-light: #ffffff;
    --ink-dark: #1e2a44;
    --art-light: #f2f4f6;
    --art-mid: #9aa6b0;
    --glass-light: #fbfcfd;
    --glass-mid: #e6eaee;
    --glass-edge: #b9c1c8;
  }
  html, body {
    margin: 0;
    padding: 0;
    width: 1200px;
    height: 3210px;
    overflow: hidden;
    background: var(--page);
  }
  .canvas {
    position: relative;
    width: 1200px;
    height: 3210px;
  }
  .sheet {
    position: absolute;
    left: 0;
    top: 0;
    width: 1200px;
    height: 3210px;
  }
</style>
</head>
<body>
<main class="canvas">
  <svg class="sheet" viewBox="0 0 1200 3210" xmlns="http://www.w3.org/2000/svg">
    <defs>
      <linearGradient id="sky" x1="0" y1="0" x2="0" y2="1">
        <stop offset="0" style="stop-color:var(--sky-top)"/>
        <stop offset="0.45" style="stop-color:var(--sky-mid)"/>
        <stop offset="0.78" style="stop-color:var(--dawn)"/>
        <stop offset="1" style="stop-color:var(--dawn)"/>
      </linearGradient>
      <radialGradient id="ship-art" cx="0.5" cy="0.55" r="0.55">
        <stop offset="0" style="stop-color:var(--art-light)"/>
        <stop offset="0.6" style="stop-color:var(--art-mid)"/>
        <stop offset="1" style="stop-color:var(--oval)" stop-opacity="0"/>
      </radialGradient>
      <linearGradient id="glass" x1="0" y1="0" x2="1" y2="0">
        <stop offset="0" style="stop-color:var(--glass-edge)"/>
        <stop offset="0.2" style="stop-color:var(--glass-light)"/>
        <stop offset="0.75" style="stop-color:var(--glass-mid)"/>
        <stop offset="1" style="stop-color:var(--glass-edge)"/>
      </linearGradient>

      <symbol id="rum-label" viewBox="90 80 1020 1390">
        <path d="M100 1460 L100 250 L240 250 C330 150 450 88 600 88 C750 88 870 150 960 250 L1100 250 L1100 1460 Z" fill="url(#sky)"/>
        <path d="M100 1130 C260 1080 420 1150 600 1140 C800 1130 930 1100 1100 1050 L1100 1460 L100 1460 Z" fill="#45b1e0"/>
        <path d="M120 1440 L120 270 L250 270 C340 176 455 108 600 108 C745 108 860 176 950 270 L1080 270 L1080 1440 Z" fill="none" stroke="#d9262b" stroke-width="6"/>
        <path d="M134 1426 L134 284 L258 284 C348 192 460 124 600 124 C740 124 852 192 942 284 L1066 284 L1066 1426 Z" fill="none" stroke="#ffffff" stroke-width="3"/>

        <ellipse cx="600" cy="790" rx="290" ry="430" fill="#ffffff"/>
        <ellipse cx="600" cy="790" rx="282" ry="422" fill="none" stroke="#3b3b3d" stroke-width="5" stroke-dasharray="5 9"/>
        <ellipse cx="600" cy="790" rx="264" ry="404" fill="#3b3b3d"/>

        <circle cx="600" cy="462" r="40" fill="none" stroke="#ffffff" stroke-width="4"/>
        <circle cx="600" cy="462" r="30" fill="none" stroke="#ffffff" stroke-width="2"/>
        <text x="600" y="632" text-anchor="middle" fill="#ffffff" font-family="'Libre Baskerville', Baskerville, serif" font-size="92" letter-spacing="6">HARKA</text>
        <line x1="430" y1="656" x2="770" y2="656" stroke="#ffffff" stroke-width="3"/>
        <text x="604" y="708" text-anchor="middle" fill="#ffffff" font-family="'Libre Baskerville', Baskerville, serif" font-size="34" letter-spacing="11">DISTILLERY</text>

        <g role="img" aria-label="Illustration of a pirate sailing ship on waves with gulls overhead">
          <ellipse cx="600" cy="990" rx="230" ry="210" fill="url(#ship-art)"/>
        </g>
        <path d="M380 1170 C470 1130 540 1190 620 1160 C700 1130 760 1150 840 1120 L840 1200 L380 1200 Z" fill="#ffffff" opacity="0.85"/>

        <text x="360" y="1306" text-anchor="middle" fill="#1e2a44" font-family="'Libre Baskerville', Baskerville, serif" font-size="32">vol.45%</text>
        <line x1="462" y1="1274" x2="462" y2="1314" stroke="#1e2a44" stroke-width="3"/>
        <text x="546" y="1306" text-anchor="middle" fill="#1e2a44" font-family="'Libre Baskerville', Baskerville, serif" font-size="32">750ml</text>
        <line x1="630" y1="1274" x2="630" y2="1314" stroke="#1e2a44" stroke-width="3"/>
        <text x="740" y="1306" text-anchor="middle" fill="#1e2a44" font-family="'Libre Baskerville', Baskerville, serif" font-size="32">90 proof</text>
        <text x="600" y="1392" text-anchor="middle" fill="#1e2a44" font-family="'Libre Baskerville', Baskerville, serif" font-size="38" letter-spacing="3">RUM DISTILLERY IN ESTONIA</text>
      </symbol>
    </defs>

    <g class="label-flat">
      <use href="#rum-label" x="90" y="80" width="1020" height="1390"/>
    </g>

    <g class="bottle-presentation">
      <path role="img" aria-label="Clear glass rum bottle" d="M486 1620 L714 1620 L712 1700 L704 1710 L704 1840 C704 1900 760 1930 820 1975 C862 2006 880 2050 880 2110 L880 3060 C880 3100 860 3120 820 3120 L380 3120 C340 3120 320 3100 320 3060 L320 2110 C320 2050 338 2006 380 1975 C440 1930 496 1900 496 1840 L496 1710 L488 1700 Z" fill="url(#glass)" stroke="#b9c1c8" stroke-width="4"/>
      <use href="#rum-label" x="346" y="2030" width="508" height="692"/>
    </g>
  </svg>
</main>
</body>
</html>
```